KORBALT

The business want a professional looking business card. We have a scetch we will add but want the extra upgrade, and would like more suggestions for variations of our business cards.

```html
<!DOCTYPE html>
<html lang="en">
<head>
<meta charset="utf-8">
<title>KORBALT – Business Card</title>
<link rel="stylesheet" href="https://fonts.googleapis.com/css2?family=Playfair+Display:wght@600;700&family=Poppins:wght@400;500&display=swap">
<style>
  :root {
    --backdrop: #ebe7df;
    --card-white: #ffffff;
    --brown: #5e451f;
    --brown-text: #5a4320;
    --gold: #c9a24a;
    --gold-light: #f3d98a;
    --gold-dark: #8a6d2c;
  }
  * { margin: 0; padding: 0; box-sizing: border-box; }
  html, body {
    width: 1200px; height: 1200px; overflow: hidden;
    background: var(--backdrop);
  }
  .canvas { position: relative; width: 1200px; height: 1200px; }

  .card { position: absolute; left: 321px; width: 568px; height: 325px; overflow: hidden; }

  /* Front */
  .card-front { top: 211px; background: var(--card-white); }
  .gold-band {
    position: absolute; left: 0; top: 0; width: 53px; height: 100%;
    background: linear-gradient(180deg, var(--gold-dark) 0%, #b8983f 25%, var(--gold-light) 50%, #b8983f 75%, var(--gold-dark) 100%);
  }
  .icon-badge {
    position: absolute; left: 35px; width: 36px; height: 36px; border-radius: 50%;
    background: var(--brown); display: flex; align-items: center; justify-content: center;
  }
  .icon-badge svg { width: 18px; height: 18px; }
  .holder-name {
    position: absolute; left: 86px; top: 58px;
    font-family: "Playfair Display", serif; font-weight: 700; font-size: 24px;
    color: var(--brown-text); letter-spacing: 0.3px; white-space: nowrap;
  }
  .holder-role {
    position: absolute; left: 86px; top: 86px;
    font-family: "Poppins", sans-serif; font-size: 16px; color: var(--brown-text);
  }
  .divider { position: absolute; left: 86px; top: 117px; width: 273px; height: 1px; background: var(--brown-text); }
  .contact-line {
    position: absolute; left: 86px;
    font-family: "Poppins", sans-serif; color: var(--brown-text); white-space: nowrap;
  }
  .contact-phone { top: 161px; font-size: 18px; font-weight: 500; letter-spacing: 0.8px; }
  .contact-mail { top: 203px; font-size: 14px; letter-spacing: 0.4px; }
  .contact-web { top: 242px; font-size: 14px; letter-spacing: 0.4px; }

  .brand-block {
    position: absolute; left: 360px; top: 192px; width: 180px; text-align: center;
  }
  .brand-name {
    font-family: "Playfair Display", serif; font-weight: 700; font-size: 30px;
    color: var(--gold); letter-spacing: 0.5px; line-height: 1;
  }
  .brand-since {
    margin-top: 6px; font-family: "Poppins", sans-serif; font-weight: 500; font-size: 11px;
    color: var(--gold); letter-spacing: 1.5px;
  }

  /* Back */
  .card-back { top: 673px; background: var(--brown); }
  .back-brand { position: absolute; left: 0; top: 126px; width: 100%; text-align: center; }
  .back-name {
    font-family: "Playfair Display", serif; font-weight: 700; font-size: 58px;
    color: var(--gold); letter-spacing: 1px; line-height: 1;
  }
  .back-since {
    margin-top: 10px; font-family: "Poppins", sans-serif; font-weight: 500; font-size: 19px;
    color: var(--gold); letter-spacing: 3px;
  }
</style>
</head>
<body>
<main class="canvas">

  <section class="card card-front" aria-label="Business card front">
    <div class="gold-band"></div>

    <div class="icon-badge" style="top:36px">
      <svg viewBox="0 0 24 24" fill="#fff" aria-hidden="true"><circle cx="12" cy="8" r="4.5"/><path d="M3.5 22c0-5 3.8-8 8.5-8s8.5 3 8.5 8z"/></svg>
    </div>
    <div class="holder-name">KORBALT R TORNVIK</div>
    <div class="holder-role">CEO &amp; Founder</div>
    <div class="divider"></div>

    <div class="icon-badge" style="top:155px">
      <svg viewBox="0 0 24 24" fill="#fff" aria-hidden="true"><path d="M6.6 10.8a15.1 15.1 0 0 0 6.6 6.6l2.2-2.2c.3-.3.7-.4 1-.2 1.1.4 2.3.6 3.6.6.6 0 1 .4 1 1V20c0 .6-.4 1-1 1A17 17 0 0 1 3 4c0-.6.4-1 1-1h3.5c.6 0 1 .4 1 1 0 1.3.2 2.5.6 3.6.1.3 0 .7-.2 1z"/></svg>
    </div>
    <div class="contact-line contact-phone">004791536204</div>

    <div class="icon-badge" style="top:194px">
      <svg viewBox="0 0 24 24" fill="none" stroke="#fff" stroke-width="2" aria-hidden="true"><rect x="3" y="5" width="18" height="14" rx="1"/><path d="M3 6l9 7 9-7"/></svg>
    </div>
    <div class="contact-line contact-mail">korbalt.llc@mailpost.com</div>

    <div class="icon-badge" style="top:233px">
      <svg viewBox="0 0 24 24" fill="none" stroke="#fff" stroke-width="1.8" aria-hidden="true"><circle cx="12" cy="12" r="9"/><ellipse cx="12" cy="12" rx="4" ry="9"/><path d="M3 12h18M4.5 7.5h15M4.5 16.5h15"/></svg>
    </div>
    <div class="contact-line contact-web">www.korbalt.llc</div>

    <div class="brand-block">
      <div class="brand-name">KORBALT</div>
      <div class="brand-since">SINCE 2026</div>
    </div>
  </section>

  <section class="card card-back" aria-label="Business card back">
    <div class="back-brand">
      <div class="back-name">KORBALT</div>
      <div class="back-since">SINCE 2026</div>
    </div>
  </section>

</main>
</body>
</html>
```